Lume Hart Co Need a custom graphic

I need to have the attached chart re-designed in a hand colored pencil format. The heading needs to be changed to "The most effective methods for hiring sales people". Do not include the background logo in the sample file.

Place the attached Lume Hart Co logo next to the most effective methods (91%)

```html
<!DOCTYPE html>
<html lang="en">
<head>
<meta charset="utf-8">
<title>The most effective methods for hiring sales people</title>
<link href="https://fonts.googleapis.com/css2?family=Patrick+Hand&family=Architects+Daughter&family=Gochi+Hand&display=swap" rel="stylesheet">
<style>
  :root {
    --paper: #ffffff;
    --grid: #a9a9a9;
    --ink: #1e1e1e;
    --pencil-red: #b5321f;
    --band: #3a3a3a;
    --band-text: #ffffff;
    --brand: #1d62b8;
  }
  html, body {
    margin: 0;
    width: 1200px;
    height: 1200px;
    overflow: hidden;
    background: var(--paper);
  }
  .chart {
    position: absolute;
    left: 0;
    top: 196px;
    width: 1200px;
    height: 808px;
    display: block;
  }
  .grid-line { stroke: var(--grid); stroke-width: 1.3; fill: none; opacity: .75; }
  .axis-tick { font-family: "Architects Daughter", cursive; font-size: 11px; fill: var(--ink); font-weight: 700; }
  .axis-title { font-family: "Gochi Hand", cursive; fill: var(--ink); font-size: 27px; letter-spacing: 1.5px; }
  .title-band { fill: var(--band); }
  .title-hatch { stroke: #6a6a6a; stroke-width: 1; }
  .title-text { font-family: "Patrick Hand", cursive; fill: var(--band-text); font-size: 27px; }
  .trend { stroke: var(--pencil-red); stroke-width: 2.2; fill: none; stroke-linejoin: round; }
  .point { fill: var(--pencil-red); }
  .label-box { fill: #fbfbfb; stroke: var(--ink); stroke-width: 2.2; stroke-dasharray: 5 1.5; }
  .label-text { font-family: "Patrick Hand", cursive; font-size: 13px; fill: var(--ink); }
  .pointer { stroke: var(--pencil-red); stroke-width: 1.6; fill: none; }
  .pointer-dashed { stroke-dasharray: 4 3; }
  .brand-name { font-family: "Patrick Hand", cursive; font-size: 23px; fill: var(--brand); }
</style>
</head>
<body>
<svg class="chart" viewBox="365 479 757 510" xmlns="http://www.w3.org/2000/svg" aria-label="Line chart: predictive validity of sales hiring methods">
  <defs>
    <marker id="arrowhead" viewBox="0 0 10 10" refX="8" refY="5" markerWidth="6" markerHeight="6" orient="auto-start-reverse">
      <path d="M0,0 L10,5 L0,10" fill="none" stroke="#b5321f" stroke-width="1.8"/>
    </marker>
    <pattern id="hatch" width="6" height="6" patternUnits="userSpaceOnUse" patternTransform="rotate(45)">
      <line x1="0" y1="0" x2="0" y2="6" class="title-hatch"/>
    </pattern>
  </defs>

  <!-- grid -->
  <g class="grid">
    <line class="grid-line" x1="452" y1="940" x2="1090" y2="940"/>
    <line class="grid-line" x1="452" y1="896" x2="1090" y2="896"/>
    <line class="grid-line" x1="452" y1="853" x2="1090" y2="853"/>
    <line class="grid-line" x1="452" y1="809" x2="1090" y2="809"/>
    <line class="grid-line" x1="452" y1="766" x2="1090" y2="766"/>
    <line class="grid-line" x1="452" y1="722" x2="1090" y2="722"/>
    <line class="grid-line" x1="452" y1="679" x2="1090" y2="679"/>
    <line class="grid-line" x1="452" y1="635" x2="1090" y2="635"/>
    <line class="grid-line" x1="452" y1="592" x2="1090" y2="592"/>
    <line class="grid-line" x1="452" y1="549" x2="1090" y2="549"/>
    <line class="grid-line" x1="452" y1="545" x2="452" y2="942"/>
    <line class="grid-line" x1="510" y1="545" x2="510" y2="942"/>
    <line class="grid-line" x1="569" y1="545" x2="569" y2="942"/>
    <line class="grid-line" x1="625" y1="545" x2="625" y2="942"/>
    <line class="grid-line" x1="683" y1="545" x2="683" y2="942"/>
    <line class="grid-line" x1="737" y1="545" x2="737" y2="942"/>
    <line class="grid-line" x1="795" y1="545" x2="795" y2="942"/>
    <line class="grid-line" x1="852" y1="545" x2="852" y2="942"/>
    <line class="grid-line" x1="908" y1="545" x2="908" y2="942"/>
    <line class="grid-line" x1="968" y1="545" x2="968" y2="942"/>
    <line class="grid-line" x1="1027" y1="545" x2="1027" y2="942"/>
  </g>

  <!-- y ticks -->
  <g class="axis-ticks">
    <text class="axis-tick" x="422" y="944">0.00</text>
    <text class="axis-tick" x="422" y="900">0.10</text>
    <text class="axis-tick" x="422" y="857">0.20</text>
    <text class="axis-tick" x="422" y="813">0.30</text>
    <text class="axis-tick" x="422" y="770">0.40</text>
    <text class="axis-tick" x="422" y="726">0.50</text>
    <text class="axis-tick" x="422" y="683">0.60</text>
    <text class="axis-tick" x="422" y="639">0.70</text>
    <text class="axis-tick" x="422" y="596">0.80</text>
    <text class="axis-tick" x="422" y="553">0.90</text>
  </g>

  <text class="axis-title" transform="translate(406 850) rotate(-90)">Predictive validity</text>
  <text class="axis-title" x="641" y="968">Hiring Method</text>

  <!-- title band -->
  <rect class="title-band" x="450" y="499" width="634" height="41"/>
  <rect x="450" y="499" width="634" height="41" fill="url(#hatch)" opacity=".5"/>
  <text class="title-text" x="767" y="528" text-anchor="middle">The most effective methods for hiring sales people</text>

  <!-- trend line -->
  <polyline class="trend" points="510,903 558,861 623,848 680,846 737,830 795,831 849,796 908,713 968,674 1027,617 1085,549"/>
  <g class="points">
    <circle class="point" cx="510" cy="903" r="3"/>
    <circle class="point" cx="558" cy="861" r="3"/>
    <circle class="point" cx="623" cy="848" r="3"/>
    <circle class="point" cx="680" cy="846" r="3"/>
    <circle class="point" cx="737" cy="830" r="3"/>
    <circle class="point" cx="795" cy="831" r="3"/>
    <circle class="point" cx="849" cy="796" r="3.5"/>
    <circle class="point" cx="908" cy="713" r="3"/>
    <circle class="point" cx="968" cy="674" r="3"/>
    <circle class="point" cx="1027" cy="617" r="3"/>
    <circle class="point" cx="1085" cy="549" r="3"/>
  </g>

  <!-- labels -->
  <g class="label">
    <rect class="label-box" x="527" y="915" width="104" height="18"/>
    <text class="label-text" x="531" y="929">Culture test, 13%</text>
    <line class="pointer" x1="527" y1="918" x2="513" y2="906" marker-end="url(#arrowhead)"/>
  </g>
  <g class="label">
    <rect class="label-box" x="463" y="819" width="108" height="18"/>
    <text class="label-text" x="474" y="833">Resume, 18%</text>
    <line class="pointer" x1="543" y1="838" x2="557" y2="857" marker-end="url(#arrowhead)"/>
  </g>
  <g class="label">
    <rect class="label-box" x="488" y="790" width="198" height="18"/>
    <text class="label-text" x="498" y="804">Behavior/personality test, 20%</text>
    <line class="pointer pointer-dashed" x1="603" y1="810" x2="621" y2="842" marker-end="url(#arrowhead)"/>
  </g>
  <g class="label">
    <rect class="label-box" x="599" y="874" width="160" height="18"/>
    <text class="label-text" x="605" y="888">Traditional interview, 20%</text>
    <line class="pointer" x1="702" y1="872" x2="686" y2="851" marker-end="url(#arrowhead)"/>
  </g>
  <g class="label">
    <rect class="label-box" x="665" y="764" width="143" height="18"/>
    <text class="label-text" x="674" y="778">Reference check, 23 %</text>
    <line class="pointer" x1="721" y1="785" x2="733" y2="823" marker-end="url(#arrowhead)"/>
  </g>
  <g class="label">
    <rect class="label-box" x="781" y="874" width="164" height="18"/>
    <text class="label-text" x="786" y="888">Emotional intelligence, 23%</text>
    <line class="pointer" x1="829" y1="872" x2="813" y2="851" marker-end="url(#arrowhead)"/>
  </g>
  <g class="label">
    <rect class="label-box" x="851" y="818" width="106" height="18"/>
    <text class="label-text" x="856" y="832">Skills test, 33%</text>
    <line class="pointer" x1="866" y1="818" x2="853" y2="801" marker-end="url(#arrowhead)"/>
  </g>
  <g class="label">
    <rect class="label-box" x="687" y="704" width="174" height="18"/>
    <text class="label-text" x="693" y="718">General mental ability, 51%</text>
    <line class="pointer" x1="865" y1="714" x2="900" y2="714" marker-end="url(#arrowhead)"/>
  </g>
  <g class="label">
    <rect class="label-box" x="626" y="661" width="288" height="18"/>
    <text class="label-text" x="634" y="675">Highly structured interview with scorecard, 57%</text>
    <line class="pointer" x1="918" y1="671" x2="957" y2="671" marker-end="url(#arrowhead)"/>
  </g>
  <g class="label">
    <rect class="label-box" x="755" y="602" width="219" height="18"/>
    <text class="label-text" x="761" y="616">Multi-measurement assessment, 71%</text>
    <line class="pointer" x1="978" y1="615" x2="1018" y2="616" marker-end="url(#arrowhead)"/>
  </g>
  <g class="label">
    <rect class="label-box" x="727" y="552" width="307" height="18"/>
    <text class="label-text" x="733" y="566">Sales-specific multi-measurement assessment, 91%</text>
    <line class="pointer" x1="1037" y1="556" x2="1070" y2="547" marker-end="url(#arrowhead)"/>
  </g>

  <!-- brand -->
  <text class="brand-name" x="953" y="597">Lume Hart Co</text>
</svg>
</body>
</html>
```